Brightpath Roster is a web based program in the sports industry. We are looking for a modern, cutting edge business card design. We are looking for a dark base and need to use three logo's on the card. Brightpath Roster, Vantora Athletic Nutrition, and Fernwick Links School.
Updates

Industry/Entity Type

Business

Requirements
Must have
• 3 logo's... Brightpath Roster... Fernwick Links School... VanTora Athletic Nutrition

```html
<!DOCTYPE html>
<html lang="en">
<head>
<meta charset="utf-8">
<title>Brightpath Roster — Business Card</title>
<link rel="stylesheet" href="https://fonts.googleapis.com/css2?family=Questrial&display=swap">
<style>
  :root {
    --orange: #ec6726;
    --orange-deep: #8a3a14;
    --ink: #1f1d1d;
    --black: #000000;
    --paper: #ffffff;
    --red: #e8393f;
    --grey: #3a3a3a;
    --social: #3aa7e0;
  }
  * { box-sizing: border-box; margin: 0; padding: 0; }
  html, body { width: 1200px; height: 1016px; overflow: hidden; background: var(--paper); }
  body { position: relative; font-family: "Questrial", "Century Gothic", sans-serif; }

  .card {
    position: absolute; top: 28px; width: 542px; height: 949px;
    background: var(--paper);
    box-shadow: 0 3px 12px rgba(0,0,0,0.35);
    overflow: hidden;
  }
  .card--front { left: 25px; }
  .card--back { left: 631px; }

  .brand {
    position: absolute; left: 0; right: 0; top: 80px;
    display: flex; align-items: center; justify-content: center; gap: 14px;
  }
  .brand__dot { width: 30px; height: 30px; border-radius: 50%; background: var(--orange); flex: none; }
  .brand__name {
    color: var(--ink); font-size: 58px; line-height: 56px; letter-spacing: -0.5px;
  }

  .front__stripe { position: absolute; left: 0; right: 0; top: 209px; height: 13px; background: var(--orange); }
  .front__field { position: absolute; left: 0; top: 222px; width: 542px; height: 706px; background: var(--black); }
  .front__art {
    position: absolute; left: 0; top: 0; width: 542px; height: 500px;
    background:
      radial-gradient(ellipse 60% 55% at 0% 25%, var(--orange-deep), rgba(0,0,0,0) 70%),
      radial-gradient(ellipse 45% 70% at 100% 55%, var(--orange-deep), rgba(0,0,0,0) 70%),
      var(--black);
  }

  .contact {
    position: absolute; left: 25px; top: 738px;
    color: var(--paper); font-size: 16px; line-height: 21.5px; letter-spacing: 0.3px;
  }
  .contact dt { display: inline; color: var(--orange); }
  .contact dd { display: inline; }
  .contact__row { display: block; }

  .front__rule {
    position: absolute; left: 25px; right: 25px; top: 850px; height: 1px;
    background: linear-gradient(90deg, rgba(255,255,255,0), #6c6c6c 50%, rgba(255,255,255,0));
  }
  .social {
    position: absolute; left: 25px; top: 877px; display: flex; align-items: center; gap: 16px;
    font-size: 29px; letter-spacing: 1.5px; color: var(--paper);
  }
  .social__square { width: 44px; height: 44px; background: var(--social); border-radius: 4px; flex: none; }
  .social__label { color: var(--orange); }

  .card__band { position: absolute; left: 0; right: 0; bottom: 0; height: 21px; background: var(--orange); }

  .back__url {
    position: absolute; left: 0; right: 0; top: 230px; text-align: center;
    font-size: 22px; letter-spacing: 2.5px; color: var(--grey);
  }
  .back__rule {
    position: absolute; left: 72px; right: 54px; top: 272px; height: 2px;
    background: linear-gradient(90deg, rgba(0,0,0,0), #9a9a9a 50%, rgba(0,0,0,0));
  }

  .partners {
    position: absolute; left: 5px; right: 5px; top: 797px; height: 134px;
    display: flex; align-items: center; justify-content: space-between;
  }
  .partner { display: flex; align-items: center; gap: 10px; width: 262px; }
  .partner__name { font-size: 19px; line-height: 23px; color: var(--ink); }
  .partner__square { width: 46px; height: 46px; background: var(--red); flex: none; }
  .partner__circle { width: 46px; height: 46px; border-radius: 50%; background: var(--red); flex: none; }
</style>
</head>
<body>

<article class="card card--front">
  <div class="brand">
    <span class="brand__dot"></span>
    <span class="brand__name">Brightpath<br>Roster</span>
  </div>
  <div class="front__stripe"></div>
  <div class="front__field">
    <div class="front__art" role="img" aria-label="Abstract decoration of orange and white circles on black"></div>
  </div>
  <dl class="contact">
    <span class="contact__row"><dt>Address:</dt> <dd>2480 Lakemont Court, Clearwater Bay, FL 33711</dd></span>
    <span class="contact__row"><dt>Phone</dt> <dd>555.318.2046</dd></span>
    <span class="contact__row"><dt>Email:</dt> <dd>sam@brightpathroster.com</dd></span>
    <span class="contact__row"><dt>website:</dt> <dd>www.brightpathroster.com</dd></span>
  </dl>
  <div class="front__rule"></div>
  <div class="social">
    <span class="social__square"></span>
    <span><span class="social__label">social:</span> @BrightpathRoster</span>
  </div>
  <div class="card__band"></div>
</article>

<article class="card card--back">
  <div class="brand">
    <span class="brand__dot"></span>
    <span class="brand__name">Brightpath<br>Roster</span>
  </div>
  <p class="back__url">www.brightpathroster.com</p>
  <div class="back__rule"></div>
  <div class="partners">
    <div class="partner">
      <span class="partner__square"></span>
      <span class="partner__name">VanTora Athletic Nutrition</span>
    </div>
    <div class="partner">
      <span class="partner__circle"></span>
      <span class="partner__name">Fernwick Links School</span>
    </div>
  </div>
  <div class="card__band"></div>
</article>

</body>
</html>
```